Tarnby Group letterhead

Hi,

I need a letterhead template created for our business. This should be done in word format and A4 size. The images need to not move in the template ie when I am adding writing in etc. and should flow on when I get to a second page.

I have attached our logo templates below.

Other details to include on the letterhead somewhere are:

0438 915 267
Max@Tarnbyelectrical.example.au
PO Box 817 Marrowvale NSW 2190
ABN: 57 318 962 407

Thanks!

```html
<!DOCTYPE html>
<html lang="en">
<head>
<meta charset="utf-8">
<title>Tarnby Group Letterhead</title>
<link href="https://fonts.googleapis.com/css2?family=Poppins:wght@400;600;700;800&display=swap" rel="stylesheet">
<style>
  :root {
    --orange: #f45300;
    --charcoal: #333333;
    --ink: #222222;
    --text: #3a3a3a;
    --paper: #ffffff;
  }
  * { margin: 0; padding: 0; box-sizing: border-box; }
  html, body { width: 848px; height: 1200px; overflow: hidden; background: var(--paper); }
  body { font-family: 'Poppins', sans-serif; color: var(--text); }
  .sheet { position: relative; width: 848px; height: 1200px; overflow: hidden; background: var(--paper); }
  .abs { position: absolute; }

  .block { position: absolute; background: var(--orange); }

  .brand-circle { left: 36px; top: 63px; width: 126px; height: 126px; border: 7px solid var(--ink); border-radius: 50%; }
  .brand-name { left: 178px; top: 80px; font-size: 39px; font-weight: 800; letter-spacing: 5px; color: var(--ink); line-height: 1; white-space: nowrap; }
  .brand-sub { left: 192px; top: 124px; width: 384px; display: flex; align-items: center; gap: 14px; }
  .brand-sub .rule { flex: 1; height: 2px; background: var(--ink); }
  .brand-sub .suffix { font-size: 24px; font-weight: 700; letter-spacing: 2px; color: var(--ink); line-height: 1; }
  .brand-tagline { left: 203px; top: 157px; font-size: 11.5px; font-weight: 600; letter-spacing: 9.8px; color: var(--ink); white-space: nowrap; }
  .brand-abn { left: 176px; width: 400px; top: 174px; text-align: center; font-size: 17px; font-weight: 700; color: var(--charcoal); }

  .header-band { left: 0; top: 257px; width: 848px; height: 11px; background: var(--charcoal); }

  .label { font-size: 14px; font-weight: 700; color: var(--charcoal); }
  .recipient-label { left: 85px; top: 326px; }
  .recipient-name { left: 85px; top: 358px; font-size: 16px; font-weight: 700; color: var(--charcoal); }
  .recipient-role { left: 85px; top: 377px; font-size: 16px; }
  .date-label { right: 87px; top: 335px; }
  .date-value { right: 87px; top: 367px; font-size: 16px; font-weight: 700; color: var(--charcoal); }

  .salutation { left: 85px; top: 457px; font-size: 17px; font-weight: 700; color: var(--charcoal); }
  .body-copy { left: 85px; top: 497px; width: 684px; font-size: 14.4px; line-height: 21.4px; }
  .body-copy p + p { margin-top: 21.4px; }

  .sign-off { left: 85px; top: 804px; font-size: 17px; font-weight: 700; color: var(--charcoal); }
  .signer-name { left: 85px; top: 896px; font-size: 18px; font-weight: 700; color: var(--charcoal); }
  .signer-role { left: 85px; top: 924px; font-size: 14.4px; }

  .footer { left: 0; top: 1049px; width: 848px; height: 103px; background: var(--charcoal); }
  .footer-strip { left: 0; top: 1152px; width: 848px; height: 10px; background: var(--orange); }

  .contact { position: absolute; top: 1085px; display: flex; gap: 12px; color: #fff; }
  .contact .icon { width: 33px; height: 33px; border-radius: 50%; background: var(--orange); display: flex; align-items: center; justify-content: center; flex: none; }
  .contact .icon svg { width: 16px; height: 16px; }
  .contact .title { font-size: 13px; font-weight: 700; line-height: 16px; }
  .contact .value { font-size: 13px; line-height: 18px; margin-top: 5px; white-space: nowrap; }
  .contact-phone { left: 85px; }
  .contact-email { left: 262px; }
  .contact-address { left: 566px; }
</style>
</head>
<body>
<div class="sheet">

  <div class="block" style="left:757px;top:11px;width:91px;height:101px"></div>
  <div class="block" style="left:700px;top:112px;width:57px;height:57px"></div>
  <div class="block" style="left:757px;top:167px;width:34px;height:34px"></div>

  <div class="abs brand-circle"></div>
  <div class="abs brand-name">TARNBY GROUP</div>
  <div class="abs brand-sub"><span class="rule"></span><span class="suffix">PTY LTD</span><span class="rule"></span></div>
  <div class="abs brand-tagline">ELECTRICAL CONTRACTORS</div>
  <div class="abs brand-abn">ABN: 57 318 962 407</div>

  <div class="abs header-band"></div>

  <div class="abs label recipient-label">TO:</div>
  <div class="abs recipient-name">Lucas Moreira</div>
  <div class="abs recipient-role">Halbrook &amp; Co. / CEO</div>
  <div class="abs label date-label">DATE:</div>
  <div class="abs date-value">12 August, 2023</div>

  <div class="abs salutation">Dear Mr. Arjun Setiawan</div>
  <div class="abs body-copy">
    <p>A letterhead is the heading at the top of a sheet of letter paper (stationery).<br>That heading usually consists of a name and an address, and a logo or corporate design, and sometimes a background pattern. The term "letterhead" is often used to refer to the whole sheet imprinted with such a heading. Many companies and individuals prefer to create a letterhead template in a word processor or other software application.</p>
    <p>This generally includes the same information as pre-printed stationery but without the additional costs involved. Letterhead can then be printed on stationery (or plain paper) as needed on a local output device or sent electronically.</p>
    <p>The term "letterhead" is often used to refer to the whole sheet imprinted with such a heading. Many companies and individuals prefer to create a letterhead template in a word processor or other software application.</p>
  </div>

  <div class="abs sign-off">Regrats,</div>
  <div class="abs signer-name">Jordan Ashby</div>
  <div class="abs signer-role">General Manager</div>

  <div class="abs footer"></div>
  <div class="abs footer-strip"></div>
  <div class="block" style="left:46px;top:970px;width:30px;height:30px"></div>
  <div class="block" style="left:0;top:1003px;width:47px;height:99px"></div>

  <div class="contact contact-phone">
    <div class="icon"><svg viewBox="0 0 24 24"><path fill="#1a1a1a" d="M6.6 10.8a15.1 15.1 0 0 0 6.6 6.6l2.2-2.2a1 1 0 0 1 1-.25 11.4 11.4 0 0 0 3.6.57 1 1 0 0 1 1 1V20a1 1 0 0 1-1 1A17 17 0 0 1 3 4a1 1 0 0 1 1-1h3.5a1 1 0 0 1 1 1c0 1.25.2 2.45.57 3.57a1 1 0 0 1-.25 1z"/></svg></div>
    <div><div class="title">Phone</div><div class="value">0438 915 267</div></div>
  </div>
  <div class="contact contact-email">
    <div class="icon"><svg viewBox="0 0 24 24"><path fill="#1a1a1a" d="M3 6h18v12H3z"/><path fill="none" stroke="#f45300" stroke-width="1.6" d="M3 6l9 7 9-7"/></svg></div>
    <div><div class="title">Email</div><div class="value">Max@Tarnbyelectrical.example.au</div></div>
  </div>
  <div class="contact contact-address">
    <div class="icon"><svg viewBox="0 0 24 24"><path fill="#1a1a1a" d="M12 2a7 7 0 0 0-7 7c0 5.2 7 13 7 13s7-7.8 7-13a7 7 0 0 0-7-7zm0 9.5A2.5 2.5 0 1 1 12 6.5a2.5 2.5 0 0 1 0 5z"/></svg></div>
    <div><div class="title">Address</div><div class="value">PO Box 817 Marrowvale NSW 2190</div></div>
  </div>

</div>
</body>
</html>
```